Tax Business Advertisement

Pemberly & Associates Tax Services - Need to develop an advertisement tool suitable for print and electronic advertising. My business provides tax preparation and audit representation for Individuals, Partnerships, Corporations, Estates, Trusts and other entities with tax reporting requirements. I recently had business cards designed by your company, design #8270451 and would need the basic information from the business card on the advertisement.

Some of the following wording may be suitable for the advertisement:

Enrolled Agents are licensed to practice by the IRS. Our services include personal and business tax return preparation, tax audits, offers in compromise, back taxes, forming new business, dissolving business, and much more. We are available to provide services in all 50 states.

Enrolled agents are the only federally licensed tax practitioners who specialize in taxation and who have unlimited rights to represent taxpayers before the IRS.

If you are just starting a business, have been in business for a long time, or just an individual who needs a Tax Professional, Pemberly & Associates Tax Services is the right choice for you.

```html
<!DOCTYPE html>
<html lang="en">
<head>
<meta charset="utf-8">
<title>Pemberly &amp; Associates Tax and Business Services</title>
<link href="https://fonts.googleapis.com/css2?family=Tinos:wght@400;700&family=Roboto:wght@400;500&display=swap" rel="stylesheet">
<style>
  :root {
    --red: #d2232a;
    --red-dark: #b01a20;
    --ink: #111111;
    --band: #1a1a1a;
    --paper: #ffffff;
    --paper-shade: #e9e9e9;
  }
  * { margin: 0; padding: 0; box-sizing: border-box; }
  html, body { width: 872px; height: 1200px; overflow: hidden; background: #ffffff; }
  body { font-family: "Tinos", "Times New Roman", serif; color: var(--ink); }

  .ad {
    position: relative;
    width: 872px; height: 1200px;
    border: 5px solid var(--red);
    background: linear-gradient(180deg, var(--paper) 0%, #f4f4f4 40%, var(--paper-shade) 100%);
    overflow: hidden;
  }
  .brand-mark {
    position: absolute; left: 70px; top: 48px;
    width: 150px; height: 130px;
    background: var(--red);
  }
  .brand-name {
    position: absolute; left: 264px; top: 64px;
    font-size: 47px; font-weight: 400; color: var(--ink); letter-spacing: 0.3px;
  }
  .brand-rule {
    position: absolute; left: 262px; top: 127px; width: 544px; height: 3px; background: var(--red);
  }
  .brand-tagline {
    position: absolute; left: 266px; top: 138px;
    font-family: "Roboto", Arial, sans-serif; font-size: 19px; font-weight: 500;
    letter-spacing: 8.6px; color: var(--ink);
  }
  .intro {
    position: absolute; left: 30px; right: 30px; top: 228px;
    text-align: center; font-size: 21px; line-height: 28px;
  }
  .rule {
    position: absolute; height: 2px; background: var(--red);
  }
  .rule--top { left: 22px; right: 22px; top: 330px; }
  .rule--mid { left: 22px; width: 578px; top: 896px; height: 1.5px; }

  .services-title {
    position: absolute; left: 30px; top: 352px;
    color: var(--red); font-size: 31px; font-weight: 700;
  }
  .services {
    position: absolute; left: 36px; top: 400px; width: 520px; list-style: none;
    font-size: 31px; line-height: 31px;
  }
  .services li { position: relative; padding-left: 34px; margin-bottom: 13px; }
  .services li::before {
    content: ""; position: absolute; left: 2px; top: 10px;
    width: 14px; height: 14px; border-radius: 50%; background: var(--red);
  }

  .coverage-map {
    position: absolute; left: 630px; top: 355px; width: 196px; height: 124px;
    background: linear-gradient(180deg, var(--red) 0%, var(--red-dark) 100%);
    border-radius: 10px 30px 22px 40px;
  }
  .coverage {
    position: absolute; left: 600px; width: 250px; top: 502px;
    text-align: center; font-size: 20px; line-height: 22px; text-transform: uppercase;
  }
  .coverage strong { color: var(--red); font-weight: 400; }

  .portrait {
    position: absolute; left: 535px; top: 578px; width: 332px; height: 560px;
    background: linear-gradient(180deg, #c08a70 0%, #8a5a45 45%, #1e1e1e 75%, #111 100%);
    border-radius: 150px 150px 0 0;
  }

  .pitch {
    position: absolute; left: 30px; top: 710px; width: 540px;
    font-size: 23px; line-height: 31px;
  }
  .pitch-close {
    position: absolute; left: 30px; top: 818px; width: 560px;
    color: var(--red); font-size: 28px; line-height: 32px; font-weight: 700;
  }

  .contacts { position: absolute; left: 36px; top: 922px; list-style: none; }
  .contacts li {
    display: flex; align-items: center; gap: 16px;
    height: 47px; font-size: 32px; font-weight: 700;
  }
  .contacts svg { width: 30px; height: 30px; flex: none; }

  .address-band {
    position: absolute; left: 0; right: 0; bottom: 0; height: 64px;
    background: var(--band); border-top: 4px solid var(--red);
    color: #ffffff; font-size: 30px; font-weight: 700;
    display: flex; align-items: center; padding-left: 20px;
  }
</style>
</head>
<body>
  <main class="ad">
    <div class="brand-mark"></div>
    <h1 class="brand-name">Pemberly &amp; Associates</h1>
    <div class="brand-rule"></div>
    <p class="brand-tagline">TAX AND BUSINESS SERVICES</p>

    <p class="intro">Enrolled Agents are licensed to practice by the IRS. We are the only federally licensed tax practitioners who specialize in taxation and who have unlimited rights to represent taxpayers before the IRS.</p>

    <div class="rule rule--top"></div>

    <h2 class="services-title">Our services include:</h2>
    <ul class="services">
      <li>Personal and business tax return preparation.</li>
      <li>Tax audits.</li>
      <li>Offers in compromise.</li>
      <li>Back taxes.</li>
      <li>Forming new business.</li>
      <li>Dissolving business</li>
    </ul>

    <div class="coverage-map" role="img" aria-label="Red map of the United States"></div>
    <p class="coverage">We are available<br>to provide services<br>in <strong>all 50 states!</strong></p>

    <div class="portrait" role="img" aria-label="Portrait photo of the tax professional in a suit and tie"></div>

    <p class="pitch">If you are just starting a business, have been in business for a long time, or just an individual who needs a Tax Professional...</p>
    <p class="pitch-close">Pemberly &amp; Associates Tax Services is the right choice for you.</p>

    <div class="rule rule--mid"></div>

    <ul class="contacts">
      <li>
        <svg viewBox="0 0 30 30" fill="none" stroke="var(--red)" stroke-width="2.5"><rect x="3" y="7" width="19" height="19"/><path d="M12 18 L26 4 L28 6 L14 20 L11 21 Z" fill="var(--red)"/></svg>
        P07395168
      </li>
      <li>
        <svg viewBox="0 0 30 30"><path d="M7 3 L12 3 L14 10 L10 13 C12 18 14 20 18 21 L21 17 L28 19 L28 24 C28 26 26 28 23 28 C13 27 4 18 3 8 C3 5 5 3 7 3 Z" fill="var(--red)"/></svg>
        (555) 214-8630
      </li>
      <li>
        <svg viewBox="0 0 30 30"><rect x="2" y="7" width="26" height="19" rx="2" fill="var(--red)"/><path d="M3 9 L15 18 L27 9" fill="none" stroke="#fff" stroke-width="2"/></svg>
        ledgerpro88@mailbox.com
      </li>
      <li>
        <svg viewBox="0 0 30 30" fill="none" stroke="var(--red)" stroke-width="2.2"><circle cx="15" cy="15" r="12"/><ellipse cx="15" cy="15" rx="5.5" ry="12"/><path d="M3 15 H27 M5 9 H25 M5 21 H25"/></svg>
        www.taxhelpeverywhere.com
      </li>
    </ul>

    <footer class="address-band">4120 Linden Road, Suite D, Maple Grove, CA 95000</footer>
  </main>
</body>
</html>
```